Carpet Cleaning Door Hanger Design Project

please design a door hanger for us. we do carpet cleaning. our company name is Brisk Loom Floorcare. our telephone number is 866-403-5176.

please make a special offer coupon.

please add bullets containing the following info-
Professional carpet, hardwood, tile & grout deep steam cleaning.
kid & pet safe.
fast drying.
100% eco friendly / toxin free products.
pet stain/s & odor control.
same day appointments.
clean uniformed employees.
and please put few other catchy lines.

please make a $20.00 of carpet cleaning coupon (restrictions apply).
please make a rooms starting at $59.99 (restrictions apply).

please also put- when you want the best for less call brisk loom floorcare.

Target Market(s)

home owners, home renters. new home buyers. new home sellers.

Industry/Entity Type

Home Improvement

Requirements
Must have
• special offer.
• double sided.
• must be a design for a door hanger.
Nice to have
• 100% satisfaction guaranteed bubble.
Should not have
• no website please

```html
<!DOCTYPE html>
<html lang="en">
<head>
<meta charset="utf-8">
<title>Brisk Loom Floorcare – Door Hangers</title>
<link href="https://fonts.googleapis.com/css2?family=Source+Sans+3:wght@400;600;700&family=Oswald:wght@500;600&display=swap" rel="stylesheet">
<style>
  :root{
    --brand-green:#3fae49;
    --deep-green:#1f7a34;
    --mid-green:#2f9440;
    --lime:#8cc63f;
    --gold:#f2b81c;
    --gold-dark:#d99a0b;
    --ink:#1f3d1f;
    --text-dark:#2a2a2a;
    --white:#ffffff;
    --stage:#e6e6e4;
  }
  *{margin:0;padding:0;box-sizing:border-box}
  html,body{width:1026px;height:1200px;overflow:hidden;background:var(--stage)}
  body{position:relative;font-family:"Source Sans 3",sans-serif}
  .hanger-neck{position:absolute;top:26px;width:388px;height:66px;filter:drop-shadow(0 -2px 4px rgba(0,0,0,.15))}
  .hanger-neck--front{left:57px}
  .hanger-neck--back{left:556px}
  .hanger{position:absolute;top:90px;width:388px;height:1008px;background:var(--white);overflow:hidden;box-shadow:0 4px 12px rgba(0,0,0,.25)}
  .hanger--front{left:57px}
  .hanger--back{left:556px}
  .hanger__art{position:absolute;inset:0}
  .hanger__title{position:absolute;top:12px;left:0;width:100%;text-align:center;color:var(--brand-green);font-weight:700;font-size:31px;letter-spacing:.5px}
  .service-pill{position:absolute;top:375px;left:20px;width:350px;height:38px;border-radius:19px;background:var(--gold);color:var(--white);font-weight:600;font-size:22px;text-align:center;line-height:38px;box-shadow:0 2px 3px rgba(0,0,0,.25)}
  .service-copy{position:absolute;left:10px;width:368px;text-align:center;color:var(--white);font-weight:600;font-size:17.5px;line-height:21px}
  .service-copy--front{top:423px}
  .service-copy--back{top:446px}
  .service-cta{position:absolute;top:466px;left:0;width:100%;text-align:center;color:#ffe23a;font-weight:700;font-size:19.5px}
  .coupon{position:absolute;left:0;width:100%}
  .coupon__label{position:absolute;left:76px;color:var(--mid-green);font-weight:600;font-size:24px;letter-spacing:.3px;white-space:nowrap}
  .coupon__price{position:absolute;font-family:"Oswald",sans-serif;font-weight:600;color:var(--ink);white-space:nowrap}
  .coupon__price small{font-size:21px}
  .coupon__note{position:absolute;font-size:14px;color:var(--text-dark)}
  .coupon--amount{top:600px}
  .coupon--amount .coupon__label{top:0}
  .coupon--amount .coupon__price{top:26px;left:74px;font-size:50px;line-height:1}
  .coupon--amount .coupon__note{top:77px;left:70px}
  .coupon--rooms{top:746px}
  .coupon--rooms .coupon__label{top:0}
  .coupon--rooms .coupon__price{top:28px;left:76px;font-size:46px;line-height:1}
  .coupon--rooms .coupon__price small{font-size:19px;margin-right:4px}
  .coupon--rooms .coupon__note{top:74px;left:70px}
  .coupon-divider{position:absolute;top:703px;left:0;width:100%;border-top:1.5px dashed #9a9a9a}
  .benefit-list{position:absolute;top:512px;left:28px;list-style:none}
  .benefit-list li{height:36px;display:flex;align-items:center;color:var(--white);font-weight:600;font-size:18px}
  .benefit-list svg{width:26px;height:24px;margin-right:9px;flex:none}
  .sign-off{position:absolute;right:15px;top:887px;text-align:right;color:var(--white)}
  .sign-off__name{color:var(--gold);font-weight:600;font-size:20px;line-height:24px}
  .sign-off__tag{font-size:13px;line-height:17px}
  .sign-off__phone{display:flex;align-items:center;justify-content:flex-end;gap:6px;color:var(--gold);font-weight:700;font-size:28px;line-height:36px;margin-top:2px}
  .sign-off__phone svg{width:26px;height:26px}
</style>
</head>
<body>

<svg width="0" height="0" style="position:absolute" aria-hidden="true">
  <defs>
    <linearGradient id="g-green" x1="0" y1="0" x2="0" y2="1">
      <stop offset="0" stop-color="#3b9a3e"/><stop offset="1" stop-color="#1f7a34"/>
    </linearGradient>
    <radialGradient id="g-green-glow" cx=".5" cy=".35" r=".8">
      <stop offset="0" stop-color="#5cb947"/><stop offset="1" stop-color="#23803a"/>
    </radialGradient>
    <linearGradient id="g-room" x1="0" y1="0" x2="1" y2="1">
      <stop offset="0" stop-color="#d9dcdf"/><stop offset=".5" stop-color="#f0e6df"/><stop offset="1" stop-color="#e9e7e2"/>
    </linearGradient>
    <linearGradient id="g-family" x1="0" y1="0" x2="1" y2="1">
      <stop offset="0" stop-color="#c9d6e6"/><stop offset=".55" stop-color="#efe3d8"/><stop offset="1" stop-color="#e6e6e6"/>
    </linearGradient>
    <linearGradient id="g-faint" x1="0" y1="0" x2="0" y2="1">
      <stop offset="0" stop-color="#f2f2f2"/><stop offset="1" stop-color="#fbfbfb"/>
    </linearGradient>
    <radialGradient id="g-globe" cx=".4" cy=".35" r=".7">
      <stop offset="0" stop-color="#7fd04a"/><stop offset="1" stop-color="#1f8a35"/>
    </radialGradient>
    <radialGradient id="g-seal" cx=".45" cy=".4" r=".6">
      <stop offset="0" stop-color="#ffe07a"/><stop offset="1" stop-color="#e0a515"/>
    </radialGradient>
    <g id="tick-box">
      <rect x="1.5" y="5.5" width="18" height="17" fill="none" stroke="#8cc63f" stroke-width="2.5"/>
      <path d="M4 13 L9 19 L24 2" fill="none" stroke="#f2b81c" stroke-width="4" stroke-linecap="round" stroke-linejoin="round"/>
    </g>
    <g id="seal">
      <circle r="56" fill="#d99a0b"/>
      <circle r="50" fill="url(#g-seal)" stroke="#fff3c4" stroke-width="2"/>
      <circle r="31" fill="none" stroke="#b57d06" stroke-width="1.5"/>
      <text y="9" text-anchor="middle" font-family="Oswald,sans-serif" font-weight="600" font-size="24" fill="#6b3f00">100%</text>
      <path id="seal-top" d="M-40 0 A40 40 0 0 1 40 0" fill="none"/>
      <path id="seal-bot" d="M-40 0 A40 40 0 0 0 40 0" fill="none"/>
      <text font-family="Source Sans 3,sans-serif" font-weight="700" font-size="11" fill="#6b3f00" letter-spacing="1"><textPath href="#seal-top" startOffset="50%" text-anchor="middle">SATISFACTION</textPath></text>
      <text font-family="Source Sans 3,sans-serif" font-weight="700" font-size="11" fill="#6b3f00" letter-spacing="1" dy="9"><textPath href="#seal-bot" startOffset="50%" text-anchor="middle">GUARANTEE</textPath></text>
    </g>
    <g id="phone-icon">
      <circle cx="13" cy="13" r="11" fill="none" stroke="#f2b81c" stroke-width="2.2"/>
      <path d="M9 7 l3 3 -1.6 1.8 c.8 1.8 2 3 3.8 3.8 L16 14 l3 3 -1.8 1.8 C12 18.5 7.5 14 7.2 8.8 Z" fill="#f2b81c"/>
    </g>
    <g id="neck">
      <path d="M0 66 L0 24 Q0 0 24 0 L364 0 Q388 0 388 24 L388 66 Z" fill="#fff"/>
      <circle cx="194" cy="34" r="24" fill="#e6e6e4" stroke="#cfcfcf" stroke-width="1"/>
      <path d="M218 34 L262 34" stroke="#b5b5b5" stroke-width="1.5"/>
    </g>
  </defs>
</svg>

<!-- Front side -->
<svg class="hanger-neck hanger-neck--front" viewBox="0 0 388 66" aria-hidden="true"><use href="#neck"/></svg>
<section class="hanger hanger--front">
  <svg class="hanger__art" width="388" height="1008" viewBox="0 0 388 1008">
    <rect width="388" height="1008" fill="#fff"/>
    <rect y="78" width="388" height="240" fill="url(#g-room)" role="img" aria-label="Photo of a smiling girl and a small dog lying on a soft white carpet"/>
    <rect y="545" width="388" height="305" fill="url(#g-faint)" role="img" aria-label="Faded photo of a carpet being vacuumed in a living room"/>
    <path d="M0 298 C90 280 170 330 260 318 C330 309 370 292 388 284 L388 544 C330 570 260 560 190 575 C120 590 60 555 0 540 Z" fill="#f2b81c"/>
    <path d="M0 308 C90 292 170 340 260 330 C330 322 370 304 388 296 L388 530 C330 555 260 545 190 560 C120 575 60 540 0 525 Z" fill="url(#g-green)"/>
    <circle cx="323" cy="99" r="28" fill="url(#g-globe)" role="img" aria-label="Eco friendly globe badge"/>
    <circle cx="340" cy="593" r="40" fill="#c9c9c9" stroke="#fff" stroke-width="4" role="img" aria-label="Carpet vacuum head close-up"/>
    <circle cx="340" cy="744" r="40" fill="#b9b9b9" stroke="#fff" stroke-width="4" role="img" aria-label="Upholstery cleaning close-up"/>
    <use href="#tick-box" transform="translate(20 590) scale(1.7)"/>
    <use href="#tick-box" transform="translate(20 736) scale(1.7)"/>
    <path d="M0 870 C100 840 250 845 388 815 L388 1008 L0 1008 Z" fill="#8cc63f"/>
    <path d="M0 882 C110 852 250 858 388 828 L388 1008 L0 1008 Z" fill="url(#g-green-glow)"/>
    <use href="#seal" x="71" y="908"/>
  </svg>

  <h1 class="hanger__title">BRISK LOOM FLOORCARE</h1>
  <div class="service-pill">CARPET &amp; UPHOLSTERY CLEANING</div>
  <p class="service-copy service-copy--front">Professional carpet, hardwood, tile, stone &amp;<br>grout deep steam cleaning</p>
  <p class="service-cta">Call us for your FREE quote today!</p>

  <div class="coupon coupon--amount">
    <p class="coupon__label">CARPET CLEANING</p>
    <p class="coupon__price">$20.00 <small>OFF</small></p>
    <p class="coupon__note">(restrictions apply)</p>
  </div>
  <div class="coupon-divider"></div>
  <div class="coupon coupon--rooms">
    <p class="coupon__label">CARPET CLEANING</p>
    <p class="coupon__price"><small>STARTING AT</small>$59.99</p>
    <p class="coupon__note">(restrictions apply)</p>
  </div>

  <div class="sign-off">
    <p class="sign-off__name">BRISK LOOM FLOORCARE</p>
    <p class="sign-off__tag">When you want the best for less,<br>Call BRISK LOOM FLOORCARE, LLC.</p>
    <p class="sign-off__phone"><svg viewBox="0 0 26 26"><use href="#phone-icon"/></svg>(866) 403-5176</p>
  </div>
</section>

<!-- Back side -->
<svg class="hanger-neck hanger-neck--back" viewBox="0 0 388 66" aria-hidden="true"><use href="#neck"/></svg>
<section class="hanger hanger--back">
  <svg class="hanger__art" width="388" height="1008" viewBox="0 0 388 1008">
    <rect width="388" height="1008" fill="#fff"/>
    <rect y="62" width="388" height="330" fill="url(#g-family)" role="img" aria-label="Photo of a mother and daughter lying on a clean carpet with family on a sofa behind"/>
    <path d="M0 380 C80 400 180 405 260 390 C320 380 360 360 388 340 L388 1008 L0 1008 Z" fill="#8cc63f"/>
    <path d="M0 392 C90 412 190 414 270 398 C330 388 365 370 388 352 L388 1008 L0 1008 Z" fill="url(#g-green-glow)"/>
    <circle cx="323" cy="99" r="28" fill="url(#g-globe)" role="img" aria-label="Eco friendly globe badge"/>
    <circle cx="304" cy="378" r="56" fill="#bfc4c6" stroke="#fff" stroke-width="4" role="img" aria-label="Steam cleaning wand on carpet"/>
    <circle cx="110" cy="785" r="46" fill="#e7dcdc" stroke="#fff" stroke-width="4" role="img" aria-label="Wine stain on white carpet"/>
    <circle cx="296" cy="785" r="46" fill="#b79366" stroke="#fff" stroke-width="4" role="img" aria-label="Coffee spill on carpet"/>
    <circle cx="203" cy="780" r="51" fill="#9aa7b1" stroke="#fff" stroke-width="4" role="img" aria-label="Tile and grout cleaning machine"/>
    <path d="M0 868 C120 835 260 835 388 868 L388 1008 L0 1008 Z" fill="#fff"/>
    <path d="M0 878 C120 845 260 845 388 878 L388 1008 L0 1008 Z" fill="#f2b81c"/>
    <path d="M0 890 C120 858 260 858 388 890 L388 1008 L0 1008 Z" fill="url(#g-green-glow)"/>
    <use href="#seal" x="74" y="908"/>
  </svg>

  <h1 class="hanger__title">BRISK LOOM FLOORCARE</h1>
  <p class="service-copy service-copy--back">Professional carpet, hardwood, tile, stone &amp;<br>grout deep steam cleaning</p>

  <ul class="benefit-list">
    <li><svg viewBox="0 0 26 24"><use href="#tick-box"/></svg>Kid &amp; pet safe</li>
    <li><svg viewBox="0 0 26 24"><use href="#tick-box"/></svg>Fast drying</li>
    <li><svg viewBox="0 0 26 24"><use href="#tick-box"/></svg>100% Eco-friendly &amp; toxic-free products</li>
    <li><svg viewBox="0 0 26 24"><use href="#tick-box"/></svg>Pet odor &amp; Pet urine removal treatment</li>
    <li><svg viewBox="0 0 26 24"><use href="#tick-box"/></svg>Same day appointments</li>
    <li><svg viewBox="0 0 26 24"><use href="#tick-box"/></svg>Clean uniformed employees</li>
  </ul>

  <div class="sign-off">
    <p class="sign-off__name">BRISK LOOM FLOORCARE</p>
    <p class="sign-off__tag">When you want the best for less,<br>Call BRISK LOOM FLOORCARE, LLC.</p>
    <p class="sign-off__phone"><svg viewBox="0 0 26 26"><use href="#phone-icon"/></svg>(866) 403-5176</p>
  </div>
</section>

</body>
</html>
```